Disability and mental health support work company requires business card

Specialising
Wrenfield Disability is a new QCAP service aimed toward QCAP participants with a history of criminal justice, psychosocial/mental health, intellectual, and cognitive disabilities.

Our focus
Focusing on providing core QCAP supports for community participation, daily activities and supported independent living.

Authentic
Likeminded people wanting to make a difference in participant's lives.

Our aim to provide holistic and empowering supports targeted towards creating independence and guidance for all participants and families.
Over 35 years of experience working with people that have psychosocial, intellectual, and cognitive disabilities.

Industry/Entity Type

disability and mental health

Contact Information for Business Card

logo - business name

Colors
0054AA
0677BA
7BADD7
CADEEF
E8F1F8
FFF300
FFF600
FEFA6F
FFFEC7
FFFEE8

Requirements
Must have
• want double sided business cards(wont let me change it)
Should not have
• any disability related pictures

```html
<!DOCTYPE html>
<html lang="en">
<head>
<meta charset="utf-8">
<title>Wrenfield Disability – Business Card</title>
<link href="https://fonts.googleapis.com/css2?family=Lato:wght@400;700;900&display=swap" rel="stylesheet">
<style>
  :root {
    --stage: #1f1f21;
    --navy: #143a63;
    --navy-deep: #11335a;
    --sky: #7badd7;
    --gold: #f0b429;
    --white: #ffffff;
    --ink: #1b1b1b;
  }
  * { margin: 0; padding: 0; box-sizing: border-box; }
  html, body { width: 1200px; height: 1015px; overflow: hidden; }
  body {
    background: var(--stage);
    font-family: "Lato", sans-serif;
    position: relative;
  }
  .card {
    position: absolute;
    left: 250px;
    width: 700px;
    height: 400px;
    overflow: hidden;
    box-shadow: 0 10px 30px rgba(0,0,0,.5);
  }

  /* Back side */
  .card-back { top: 60px; background: var(--navy); }
  .back-pattern {
    position: absolute; inset: 0;
    background: radial-gradient(ellipse at 50% 50%, #1a4573 0%, var(--navy-deep) 75%);
  }
  .back-name {
    position: absolute; left: 0; right: 0; top: 182px;
    text-align: center;
    font-weight: 900; font-size: 32px; letter-spacing: 2px;
    color: var(--sky);
  }

  /* Front side */
  .card-front { top: 545px; background: var(--white); }
  .band-left {
    position: absolute; left: 0; top: 185px; width: 470px; height: 115px;
    background: var(--navy);
  }
  .band-right {
    position: absolute; right: 0; top: 105px; width: 180px; height: 80px;
    background: var(--navy);
  }
  .seal-gap {
    position: absolute; left: 388px; top: 58px; width: 256px; height: 256px;
    border-radius: 50%; background: var(--white);
  }
  .seal {
    position: absolute; left: 400px; top: 70px; width: 232px; height: 232px;
    border-radius: 50%; background: var(--navy);
    border: 3px solid var(--sky);
    display: flex; align-items: center; justify-content: center;
    text-align: center;
  }
  .seal-name {
    font-weight: 900; font-size: 27px; line-height: 1.15; letter-spacing: 1px;
    color: var(--sky);
  }
  .person { position: absolute; left: 60px; top: 88px; }
  .person-name {
    font-weight: 900; font-size: 26px; letter-spacing: .5px;
    color: var(--navy); text-transform: uppercase;
  }
  .person-role { font-size: 22px; color: var(--gold); margin-top: 2px; }
  .contacts {
    position: absolute; left: 110px; top: 197px;
    list-style: none; color: var(--white); font-size: 20px; line-height: 23px;
  }
  .contacts li { display: flex; align-items: center; gap: 12px; }
  .contacts svg { width: 18px; height: 18px; flex: none; }
  .address {
    position: absolute; left: 130px; top: 320px;
    font-size: 21px; line-height: 27px; color: var(--ink);
  }
</style>
</head>
<body>

<section class="card card-back">
  <div class="back-pattern" role="img" aria-label="Repeating faint pattern of the company mark across the navy background"></div>
  <div class="back-name">WRENFIELD DISABILITY</div>
</section>

<section class="card card-front">
  <div class="band-left"></div>
  <div class="band-right"></div>
  <div class="seal-gap"></div>
  <div class="seal"><span class="seal-name">WRENFIELD<br>DISABILITY</span></div>

  <div class="person">
    <div class="person-name">Marcus Ellery</div>
    <div class="person-role">Managing Director</div>
  </div>

  <ul class="contacts">
    <li>
      <svg viewBox="0 0 24 24" fill="none" stroke="#7badd7" stroke-width="2"><path d="M5 3h4l2 5-3 2a11 11 0 0 0 6 6l2-3 5 2v4a2 2 0 0 1-2 2A17 17 0 0 1 3 5a2 2 0 0 1 2-2z"/></svg>
      044-123 456 789
    </li>
    <li>
      <svg viewBox="0 0 24 24" fill="none" stroke="#7badd7" stroke-width="2"><rect x="6" y="2" width="12" height="20" rx="2"/><line x1="11" y1="18" x2="13" y2="18"/></svg>
      044-123 456 789
    </li>
    <li>
      <svg viewBox="0 0 24 24" fill="none" stroke="#7badd7" stroke-width="2"><rect x="2" y="5" width="20" height="14"/><path d="M2 5l10 8 10-8"/></svg>
      info@wrenfieldcare.com
    </li>
    <li>
      <svg viewBox="0 0 24 24" fill="none" stroke="#7badd7" stroke-width="2"><circle cx="12" cy="12" r="10"/><path d="M2 12h20M12 2c3 3 3 17 0 20M12 2c-3 3-3 17 0 20"/></svg>
      www.wrenfieldcare.com
    </li>
  </ul>

  <div class="address">421, Address line here<br>Country Name, 45452</div>
</section>

</body>
</html>
```